Family Farm Looking for meat label

We have a small farm in Italy with two types of cow "Piemontese" and "Pezzata Rossa Valdostana". We need label ( about 5x5 cm) to put on the boxes and on every single piece of meat.

Target Market(s)

private client

Industry/Entity Type

family farm

Colors

Designer to choose colors to be used in the design.

Requirements
Must have
• to write "Azienda Agricola Il Mulinetto" and the cow like our cow not differently. the Piemontese breed cow has the typical physical shapes as in the photo. No photo on the label just a drawing o something like that.
Nice to have
• just a one label, clear, fine and clean . Maybe with pastel color or watercolor. We are a small family farm.
Should not have
• no photo, no another type of cow

```html
<!DOCTYPE html>
<html lang="it">
<head>
<meta charset="utf-8">
<title>Il Mulinetto – Meat Label</title>
<link rel="stylesheet" href="https://fonts.googleapis.com/css2?family=Abril+Fatface&family=Alfa+Slab+One&family=Montserrat:wght@600;800&family=Oswald:wght@600&display=swap">
<style>
  :root {
    --green-dark: #076834;
    --green: #05a14a;
    --green-soft: #3dbb7d;
    --orange: #ef744a;
    --peach: #f6c3a8;
    --red: #ee4b4f;
    --ink: #1b1b1b;
    --slate: #3a3f47;
    --white: #ffffff;
    --page: #ffffff;
  }
  html, body {
    margin: 0;
    width: 713px;
    height: 1200px;
    overflow: hidden;
    background: var(--page);
  }
  .canvas {
    position: relative;
    width: 713px;
    height: 1200px;
  }
  .label {
    position: absolute;
    left: 56px;
    top: 300px;
    width: 600px;
    height: 600px;
    box-shadow: 5px 5px 6px rgba(0,0,0,0.35);
  }
  .label svg { display: block; width: 100%; height: 100%; }
  .weight-num { font-family: "Oswald", sans-serif; font-weight: 600; fill: var(--white); }
  .brand-name { font-family: "Oswald", sans-serif; font-weight: 600; fill: var(--green-dark); letter-spacing: 1px; }
  .claim { font-family: "Montserrat", sans-serif; font-weight: 800; fill: var(--ink); letter-spacing: 2px; }
  .banner-text { font-family: "Alfa Slab One", serif; fill: var(--white); }
  .farm-name {
    font-family: "Abril Fatface", serif;
    fill: var(--green-dark);
    stroke: var(--white);
    stroke-width: 8px;
    paint-order: stroke;
  }
  .body-copy { font-family: "Montserrat", sans-serif; font-weight: 600; fill: var(--ink); }
</style>
</head>
<body>
<main class="canvas">
  <section class="label">
    <svg viewBox="0 0 1084 1084" xmlns="http://www.w3.org/2000/svg">
      <defs>
        <linearGradient id="bg-fade" x1="0" y1="0" x2="0" y2="1">
          <stop offset="0" stop-color="var(--green-soft)"/>
          <stop offset="0.36" stop-color="#dff2e6"/>
          <stop offset="0.6" stop-color="#ffffff"/>
          <stop offset="0.75" stop-color="var(--peach)"/>
          <stop offset="1" stop-color="var(--orange)"/>
        </linearGradient>
        <radialGradient id="animal-tone" cx="0.5" cy="0.5" r="0.6">
          <stop offset="0" stop-color="#e6e6e6"/>
          <stop offset="1" stop-color="#9a9a9a"/>
        </radialGradient>
        <path id="claim-arc" d="M250,320 Q560,150 880,330"/>
      </defs>

      <rect class="label-bg" width="1084" height="1084" fill="url(#bg-fade)"/>

      <path class="weight-corner-edge" d="M0,0 H415 Q120,120 0,380 Z" fill="var(--white)"/>
      <path class="weight-corner" d="M0,0 H400 Q100,110 0,305 Z" fill="var(--green-dark)"/>
      <text class="weight-num" x="90" y="96" font-size="78" text-anchor="middle">500</text>
      <text class="weight-num" x="90" y="142" font-size="44" text-anchor="middle">gm</text>

      <text class="brand-name" x="548" y="158" font-size="58" text-anchor="middle">IL MULINETTO</text>

      <g class="origin-badge">
        <circle cx="953" cy="110" r="76" fill="var(--slate)"/>
        <circle cx="953" cy="110" r="64" fill="var(--white)"/>
        <path d="M891,150 L870,178 L1036,178 L1015,150 Z" fill="var(--slate)"/>
      </g>

      <text class="claim" font-size="46">
        <textPath href="#claim-arc" startOffset="50%" text-anchor="middle">100% NATURAL PRODUCT</textPath>
      </text>

      <g class="oval-frame">
        <ellipse cx="542" cy="505" rx="388" ry="232" fill="var(--white)" opacity="0.55"/>
        <ellipse cx="542" cy="505" rx="388" ry="233" fill="none" stroke="var(--green)" stroke-width="3"/>
        <ellipse cx="542" cy="505" rx="374" ry="220" fill="none" stroke="var(--red)" stroke-width="8"/>
        <ellipse cx="542" cy="505" rx="356" ry="204" fill="none" stroke="var(--green)" stroke-width="3"/>
      </g>

      <ellipse class="cattle-art" role="img" aria-label="Drawing of a Piemontese bull standing on grass"
               cx="565" cy="520" rx="215" ry="135" fill="url(#animal-tone)" opacity="0.75"/>

      <g class="ribbon">
        <path d="M125,735 L235,712 L290,808 L150,832 L203,774 Z" fill="var(--green)" stroke="var(--ink)" stroke-width="5"/>
        <path d="M960,735 L850,712 L795,808 L935,832 L882,774 Z" fill="var(--green)" stroke="var(--ink)" stroke-width="5"/>
        <path d="M225,660 Q540,632 858,672 L846,762 Q540,728 240,748 Z" fill="var(--green)" stroke="var(--ink)" stroke-width="6"/>
        <path id="banner-arc" d="M250,728 Q540,700 840,735" fill="none"/>
        <text class="banner-text" font-size="62">
          <textPath href="#banner-arc" startOffset="50%" text-anchor="middle" textLength="570" lengthAdjust="spacingAndGlyphs">PREMIUM ITALIAN MEAT</textPath>
        </text>
      </g>

      <text class="farm-name" x="542" y="840" font-size="92" text-anchor="middle">Azienda</text>
      <text class="farm-name" x="542" y="940" font-size="84" text-anchor="middle" textLength="900" lengthAdjust="spacingAndGlyphs">Agricola Il Mulinetto</text>

      <text class="body-copy" font-size="15.5" text-anchor="middle">
        <tspan x="542" y="996">Lorem ipsum dolor sit amet, consectetuer adipiscing elit, sed diam nonummy nibh</tspan>
        <tspan x="542" y="1019">euismod tincidunt ut laoreet dolore magna aliquam erat volutpat. Ut wisi enim ad minim</tspan>
        <tspan x="542" y="1042">veniam, quis nostrud exerci tation ullamcorper suscipit lobortis nisl ut aliquip ex ea</tspan>
      </text>
    </svg>
  </section>
</main>
</body>
</html>
```